Business Card Design

We are a church looking for marketing business card. Contact info Pastors name and a map on the back. Service times. Looking for something to grab attention. Not looking for personal card more of a generic card to pass out to new potential visitors.
Updates

Industry/Entity Type

Marketing

Contact Information for Business Card

Harbor Stone Fellowship Church
418 Willow Crest Pkwy suite 3-D Jonesboro GA 30299
(555)314-8862
Hsfcwebsite.org
Pastor Howard Pemberly
Sunday 12:00 pm
Wednesday prayer call 9:30 pm 5558807342 conference #8364152

```html
<!DOCTYPE html>
<html lang="en">
<head>
<meta charset="utf-8">
<title>Harbor Stone Fellowship Church – Business Card</title>
<link rel="stylesheet" href="https://fonts.googleapis.com/css2?family=Lato:wght@400;700&display=swap">
<style>
  :root {
    --brown: #3e2a1f;
    --paper: #ffffff;
    --ink-light: #ffffff;
  }
  * { margin: 0; padding: 0; box-sizing: border-box; }
  html, body {
    width: 1200px;
    height: 702px;
    overflow: hidden;
    background: var(--paper);
  }
  .card {
    position: relative;
    width: 1200px;
    height: 702px;
    background: var(--paper);
    font-family: "Lato", sans-serif;
    color: var(--brown);
  }
  .brand {
    position: absolute;
    left: 72px;
    top: 196px;
    width: 560px;
    display: flex;
    align-items: center;
    gap: 18px;
    white-space: nowrap;
  }
  .brand-mark {
    flex: 0 0 auto;
    width: 48px;
    height: 48px;
    background: var(--brown);
  }
  .brand-name {
    font-size: 31px;
    font-weight: 700;
    line-height: 1.15;
    color: var(--brown);
  }
  .pastor {
    position: absolute;
    left: 660px;
    top: 132px;
    font-size: 42px;
    font-weight: 700;
    letter-spacing: -0.5px;
    white-space: nowrap;
  }
  .schedule {
    position: absolute;
    left: 662px;
    top: 272px;
    list-style: none;
    font-size: 31px;
    font-weight: 400;
    line-height: 41px;
    white-space: nowrap;
  }
  .footer-band {
    position: absolute;
    left: 0;
    top: 450px;
    width: 1200px;
    height: 252px;
    background: var(--brown);
    color: var(--ink-light);
    text-align: center;
    padding-top: 43px;
  }
  .footer-band p {
    font-size: 31px;
    line-height: 37px;
    font-weight: 400;
    white-space: nowrap;
  }
</style>
</head>
<body>
  <div class="card">
    <div class="brand">
      <span class="brand-mark"></span>
      <span class="brand-name">Harbor Stone Fellowship Church</span>
    </div>

    <h1 class="pastor">Pastor Howard Pemberly</h1>

    <ul class="schedule">
      <li>Sunday 12:00 pm</li>
      <li>Wednesday prayer call 9:30 pm</li>
      <li>PH : 5558807342</li>
      <li>Conference #8364152</li>
    </ul>

    <footer class="footer-band">
      <p class="church-name">Harbor Stone Fellowship Church</p>
      <p class="address">418 Willow Crest Pkwy suite 3-D Larkfield WN 30299</p>
      <p class="phone">PH : (555)314-8862</p>
      <p class="website">Website : hsfcwebsite.org</p>
    </footer>
  </div>
</body>
</html>
```